R7M Meridian Business Card Design

We need a business card created for our New Business "R7M Meridian"<br/><br/>The business card design is up to you however the following information must be on the business card:<br/><br/>Front of the business card -<br/>Email :dorianv@r7mmeridian.nz<br/>Mobile: +64 (0) 22 4871 659<br/>Website: www.r7mmeridian.nz<br/>Card Owner Name: Dorian Valcourt<br/>Company Title: Business Development Manager<br/>Slogan: "Crafted for every venture". <br/>Logo On the front attached to the design brief<br/><br/>On the back: <br/>Space on the back for 4 more versions of the logo across the bottom of the card indicating different subsidiary brands - R7M Coffee, R7M Arts, R7M ?? (The card will be used for all of these brands - We Will add the extra subsidiary logos to the design once the design is finished (We are a graphics design team). <br/><br/>Other than that we want a premium feeling logo that remains universally usable depending on the business entity that we are using the card for. The use of bright bold colours would be great but we still want the card to feel premium.
Target Market(s)
Gift Design and Manufacturing Companies
Contact Information for Business Card
Front of the business card -
Email :dorianv@r7mmeridian.nz
Mobile: +64 (0) 22 4871 659
Website: www.r7mmeridian.nz
Card Owner Name: Dorian Valcourt
Company Title: Business Development Manager
Slogan: "Crafted for every venture".
Logo On the front attached to the design brief

```html
<!DOCTYPE html>
<html lang="en">
<head>
<meta charset="utf-8">
<title>R7M Meridian Business Card</title>
<link rel="stylesheet" href="https://fonts.googleapis.com/css2?family=Montserrat:wght@500;600;700&display=swap">
<style>
  :root {
    --bg: #e6e8e9;
    --paper: #f7f7f5;
    --brand-blue: #2f3fae;
    --edge-navy: #1e2672;
    --ink: #2b2b2b;
  }
  * { box-sizing: border-box; margin: 0; padding: 0; }
  html, body { width: 1200px; height: 824px; overflow: hidden; }
  body {
    background: var(--bg);
    font-family: "Montserrat", Arial, sans-serif;
    color: var(--ink);
    display: flex;
    align-items: center;
    justify-content: center;
    gap: 56px;
  }
  .card {
    width: 504px;
    height: 288px;
    background: var(--paper);
    border-bottom: 6px solid var(--edge-navy);
    box-shadow: 0 10px 24px rgba(0,0,0,0.12);
    position: relative;
  }
  /* Front: contact side */
  .identity {
    position: absolute;
    top: 34px;
    right: 30px;
    text-align: right;
  }
  .identity .name {
    font-size: 19px;
    font-weight: 600;
    color: var(--brand-blue);
    letter-spacing: 0.3px;
  }
  .identity .role {
    margin-top: 3px;
    font-size: 11px;
    font-weight: 600;
    color: var(--ink);
  }
  .contact-list {
    position: absolute;
    left: 30px;
    top: 112px;
    list-style: none;
  }
  .contact-list li {
    display: flex;
    align-items: center;
    gap: 9px;
    font-size: 12px;
    font-weight: 500;
    line-height: 18px;
  }
  .contact-list svg { width: 11px; height: 11px; flex: none; }
  /* Back: brand side */
  .brand {
    position: absolute;
    inset: 0;
    display: flex;
    flex-direction: column;
    align-items: center;
    justify-content: center;
    gap: 12px;
  }
  .brand-name {
    font-size: 32px;
    font-weight: 700;
    color: var(--brand-blue);
    letter-spacing: 0.5px;
  }
  .slogan {
    font-size: 10px;
    font-weight: 700;
    letter-spacing: 1.5px;
    text-transform: uppercase;
    color: var(--ink);
  }
</style>
</head>
<body>
  <section class="card card-front">
    <div class="identity">
      <p class="name">Dorian Valcourt</p>
      <p class="role">Business Development Manager</p>
    </div>
    <ul class="contact-list">
      <li>
        <svg viewBox="0 0 12 12" aria-hidden="true"><rect x="3" y="0.8" width="6" height="10.4" rx="1" fill="none" stroke="var(--brand-blue)" stroke-width="1.4"/></svg>
        +64 (0) 22 4871 659
      </li>
      <li>
        <svg viewBox="0 0 12 12" aria-hidden="true"><rect x="0.5" y="2.5" width="11" height="7" fill="var(--brand-blue)"/><path d="M0.5 2.5 L6 6.5 L11.5 2.5" fill="none" stroke="#fff" stroke-width="1"/></svg>
        dorianv@r7mmeridian.nz
      </li>
      <li>
        <svg viewBox="0 0 12 12" aria-hidden="true"><circle cx="6" cy="6" r="5.5" fill="var(--brand-blue)"/><path d="M1 6 H11 M6 0.5 C3.5 3 3.5 9 6 11.5 M6 0.5 C8.5 3 8.5 9 6 11.5" fill="none" stroke="#fff" stroke-width="0.8"/></svg>
        www.r7mmeridian.nz
      </li>
    </ul>
  </section>

  <section class="card card-back">
    <div class="brand">
      <p class="brand-name">R7M Meridian</p>
      <p class="slogan">Crafted for every venture</p>
    </div>
  </section>
</body>
</html>
```